Workout book cover design: Looking for Simple Classic Cover

I need a book cover design for "The Steady Middle". A book on exercises to strengthen the pelvic floor. Basically it's exercises for your torso and hips. I want something tasteful and classic looking.

I like this book cover design: http://www.pagelorn-books.example/Calm-Starters-Gentle-Routines-Ease-ebook/dp/Q93KX7TM41/ref=sr_1_40?ie=UTF8&qid=2958173306&sr=8-40&keywords=exercise+books

Book Title: The Steady Middle
Description to go under title: I'm working on that now and will have ready by the end of the project. (The hidden world of pelvic floor training. Discover the best exercises for creating a strong core, hips and pelvis today!)

Target Market(s)

Mostly women 35-65 and men 60+

Industry/Entity Type

Health And Wellness

Requirements
Must have
• ebook dementions: 1536 x 2048 I think works for all the online publishing companies
• 8x10 for print
Nice to have
• I like this book cover design: http://www.pagelorn-books.example/Calm-Starters-Gentle-Routines-Ease-ebook/dp/Q93KX7TM41/ref=sr_1_40?ie=UTF8&qid=2958173306&sr=8-40&keywords=exercise+books
• This cover is also ok, but no shiny. http://www.pagelorn-books.example/Bedrock-Renew-The-Climb-Poise/dp/4827305519/ref=sr_1_2?ie=UTF8&qid=2958176642&sr=8-2&keywords=foundation+book
Should not have
• I do not like this cover, it's crowded. http://www.pagelorn-books.example/Gym-Drills-Selfweight-flexing-drills-ebook/dp/Q71RWJZNHE/ref=sr_1_2?ie=UTF8&qid=2958174418&sr=8-2&keywords=workout+books
• I do not want anyone on the cover making eye contact.

```html
<!DOCTYPE html>
<html lang="en">
<head>
<meta charset="utf-8">
<title>The Steady Middle – Book Cover</title>
<link rel="stylesheet" href="https://fonts.googleapis.com/css2?family=Bebas+Neue&display=swap">
<style>
  :root {
    --page-bg: #ffffff;
    --wall-light: #f5f5f4;
    --wall-mid: #dededc;
    --floor-light: #d6c0a0;
    --floor-dark: #a98a6b;
    --title-red: #e00000;
    --ink-black: #111111;
    --band-black: #222222;
    --band-text: #ffffff;
    --photo-top: #eef2f7;
    --photo-mid: #9bbbe0;
    --photo-blue: #2a78cc;
  }
  * { margin: 0; padding: 0; box-sizing: border-box; }
  html, body {
    width: 1000px;
    height: 1200px;
    overflow: hidden;
    background: var(--page-bg);
  }
  .canvas {
    position: relative;
    width: 1000px;
    height: 1200px;
    background: var(--page-bg);
    font-family: "Bebas Neue", "Oswald", "Arial Narrow", sans-serif;
    font-weight: 400;
  }
  .cover {
    position: absolute;
    left: 147px;
    top: 40px;
    width: 735px;
    height: 1103px;
    overflow: hidden;
  }
  .cover-wall {
    position: absolute;
    left: 0; top: 0;
    width: 735px;
    height: 832px;
    background: radial-gradient(ellipse at 50% 40%, var(--wall-light) 0%, var(--wall-light) 55%, var(--wall-mid) 100%);
  }
  .cover-floor {
    position: absolute;
    left: 0; top: 832px;
    width: 735px;
    height: 153px;
    background: linear-gradient(180deg, var(--floor-dark) 0%, var(--floor-light) 40%, var(--floor-light) 100%);
  }
  .author-name {
    position: absolute;
    left: 0; top: 46px;
    width: 735px;
    text-align: center;
    font-size: 72px;
    line-height: 1;
    letter-spacing: 2px;
    color: var(--ink-black);
  }
  .author-name span {
    display: inline-block;
    border-bottom: 3px solid var(--ink-black);
  }
  .hero-photo {
    position: absolute;
    left: 113px;
    top: 145px;
    width: 516px;
    height: 360px;
    border-radius: 6px;
    background: linear-gradient(180deg, var(--photo-top) 0%, var(--photo-mid) 55%, var(--photo-blue) 100%);
  }
  .title {
    position: absolute;
    left: 0; width: 735px;
    text-align: center;
    text-transform: uppercase;
    line-height: 1;
    white-space: nowrap;
    font-weight: 400;
  }
  .title-first {
    top: 519px;
    font-size: 257px;
    color: var(--title-red);
  }
  .title-middle {
    top: 747px;
    font-size: 101px;
    color: var(--ink-black);
    display: flex;
    justify-content: center;
    align-items: center;
    gap: 20px;
  }
  .title-middle::before,
  .title-middle::after {
    content: "";
    width: 72px;
    height: 3px;
    margin-top: -6px;
    background: var(--ink-black);
  }
  .title-last {
    top: 822px;
    font-size: 183px;
    color: var(--title-red);
  }
  .tagline-band {
    position: absolute;
    left: 0; top: 985px;
    width: 735px;
    height: 118px;
    background: var(--band-black);
    color: var(--band-text);
    display: flex;
    flex-direction: column;
    justify-content: center;
    align-items: center;
    text-transform: uppercase;
    font-size: 38px;
    line-height: 48px;
    text-align: center;
  }
</style>
</head>
<body>
  <main class="canvas">
    <section class="cover">
      <div class="cover-wall" role="img" aria-label="Whitewashed brick wall backdrop"></div>
      <div class="cover-floor" role="img" aria-label="Light wooden plank floor"></div>

      <p class="author-name"><span>AUTHOR’S NAME</span></p>

      <div class="hero-photo" role="img" aria-label="Photo of a woman in black workout clothes lying back on a blue exercise ball, lifting dumbbells overhead on a blue mat"></div>

      <h1>
        <span class="title title-first">The</span>
        <span class="title title-middle">Steady</span>
        <span class="title title-last">Middle</span>
      </h1>

      <p class="tagline-band">
        <span>Discover the best exercises for</span>
        <span>creating a strong core, hips and pelvis today!</span>
      </p>
    </section>
  </main>
</body>
</html>
```